Stationary for an International Church

We need a design for various stationery items - letters/envelopes, Word/PowerPoint pages, based on
- the MBF Logo
- the primary color "bright turquoise" ("vivid cyan"), hex #08e8de
- the font family: Frutiger 55 Roman
To get an image of our organization, please visit velmarhall.org, recent blog entries at https://www.velmarhall.org/blog or annual reports at Downloads

Target Market(s)

Congregation and business partners of the Chruch

Font styles to use
Other font styles liked:
• requirement: Frutiger 55 Roman

Colors
33b8a4

Requirements
Must have
• simple, modern design, a bit unique

```html
<!DOCTYPE html>
<html lang="en">
<head>
<meta charset="utf-8">
<title>Velmar Hall Church — Letterhead</title>
<link rel="stylesheet" href="https://fonts.googleapis.com/css2?family=Open+Sans:wght@400&family=Roboto:wght@400&display=swap">
<style>
  :root {
    --backdrop: #dedede;
    --paper: #f8f8f8;
    --brand: #5bc0c4;
    --ink: #4a4a4a;
    --ink-soft: #555555;
    --signature-tone: #e4e4e4;
  }
  * { box-sizing: border-box; margin: 0; padding: 0; }
  html, body {
    width: 1153px;
    height: 1200px;
    overflow: hidden;
    background: var(--backdrop);
  }
  .letterhead {
    position: absolute;
    left: 168px;
    top: 30px;
    width: 817px;
    height: 1140px;
    background: var(--paper);
    box-shadow: 0 6px 24px rgba(0,0,0,0.12);
    font-family: "Open Sans", Arial, sans-serif;
    color: var(--ink);
  }
  .brand {
    position: absolute;
    left: 87px;
    top: 150px;
    width: 170px;
    text-align: center;
    color: var(--brand);
  }
  .brand-mark {
    display: block;
    width: 18px;
    height: 18px;
    margin: 0 auto 10px;
    background: var(--brand);
  }
  .brand-name {
    font-size: 11.2px;
    letter-spacing: 1.6px;
    white-space: nowrap;
  }
  .brand-rule {
    height: 1.5px;
    background: var(--brand);
    margin: 7px 0 6px;
  }
  .brand-tagline {
    font-size: 10.6px;
    letter-spacing: 1.1px;
  }
  .letter-body {
    position: absolute;
    left: 73px;
    top: 293px;
    width: 670px;
    font-size: 14.6px;
    line-height: 21.9px;
  }
  .letter-body p { margin-bottom: 22px; text-align: justify; }
  .letter-body .salutation,
  .letter-body .closing { text-align: left; }
  .signature {
    position: absolute;
    left: 73px;
    top: 870px;
    width: 100px;
    height: 93px;
    background: var(--signature-tone);
    border-radius: 4px;
  }
  .contact {
    position: absolute;
    top: 1030px;
    font-family: "Roboto", Arial, sans-serif;
    font-size: 16.6px;
    line-height: 23px;
    color: var(--ink-soft);
  }
  .contact-phone { left: 73px; }
  .contact-web { left: 275px; }
  .contact-address { right: 74px; text-align: right; }
  .contact-line { display: flex; align-items: center; gap: 6px; white-space: nowrap; }
  .contact-line svg { width: 17px; height: 17px; fill: var(--brand); flex: none; }
</style>
</head>
<body>
  <main class="letterhead">
    <header class="brand">
      <span class="brand-mark"></span>
      <div class="brand-name">VELMAR HALL CHURCH</div>
      <div class="brand-rule"></div>
      <div class="brand-tagline">God’s house, my home</div>
    </header>

    <section class="letter-body">
      <p class="salutation">Dear customer,</p>
      <p>Lorem ipsum dolor sit amet, consectetur adipisicing elit, sed do eiusmod tempor incididunt ut labore et dolore magna aliqua. Ut enim ad minim veniam, quis nostrud exercitation ullamco laboris nisi ut aliquip ex ea commodo consequat. Duis aute irure dolor in reprehenderit in voluptate velit esse cillum dolore eu fugiat nulla pariatur. Excepteur sint occaecat cupidatat non proident, sunt in culpa qui officia deserunt mollit anim id est laborum.</p>
      <p>Lorem ipsum dolor sit amet, consectetur adipisicing elit, sed do eiusmod tempor incididunt ut labore et dolore magna aliqua. Ut enim ad minim veniam, quis nostrud exercitation ullamco laboris nisi ut aliquip ex ea commodo consequat. Duis aute irure dolor in reprehenderit in voluptate velit esse cillum dolore eu fugiat nulla pariatur. Excepteur sint occaecat cupidatat non proident, sunt in culpa qui officia deserunt mollit anim id est laborum.</p>
      <p>Lorem ipsum dolor sit amet, consectetur adipisicing elit, sed do eiusmod tempor incididunt ut labore et dolore magna aliqua. Ut enim ad minim veniam, quis nostrud exercitation ullamco laboris nisi ut aliquip ex ea commodo consequat. Duis aute irure dolor in reprehenderit in voluptate velit esse cillum dolore eu fugiat nulla pariatur. Excepteur sint occaecat cupidatat non proident, sunt in culpa qui officia deserunt mollit anim id est laborum.</p>
      <p>Lorem ipsum dolor sit amet, consectetur adipisicing elit, sed do eiusmod tempor incididunt ut labore et dolore magna aliqua. Ut enim ad minim veniam, quis nostrud exercitation ullamco laboris nisi ut aliquip ex ea commodo consequat. Duis aute irure dolor in reprehenderit.</p>
      <p class="closing">Yours Sincerely,</p>
    </section>

    <div class="signature" role="img" aria-label="Handwritten signature of the sender"></div>

    <footer>
      <div class="contact contact-phone">
        <div class="contact-line">
          <svg viewBox="0 0 24 24" aria-hidden="true"><path d="M6.6 10.8a15.1 15.1 0 0 0 6.6 6.6l2.2-2.2a1 1 0 0 1 1-.25 11.4 11.4 0 0 0 3.6.57 1 1 0 0 1 1 1V20a1 1 0 0 1-1 1A17 17 0 0 1 3 4a1 1 0 0 1 1-1h3.5a1 1 0 0 1 1 1c0 1.25.2 2.45.57 3.57a1 1 0 0 1-.25 1z"/></svg>
          <span>(03) 5550-0147</span>
        </div>
        <div class="contact-line">
          <svg viewBox="0 0 24 24" aria-hidden="true"><path d="M6 2h12v5H6zM4 8h16a2 2 0 0 1 2 2v7h-4v5H6v-5H2v-7a2 2 0 0 1 2-2zm4 8v4h8v-4z"/></svg>
          <span>(03) 5550-1942</span>
        </div>
      </div>
      <div class="contact contact-web">
        <div class="contact-line">
          <svg viewBox="0 0 24 24" aria-hidden="true"><path d="M2 5h20v14H2zm2 2v.4l8 5.2 8-5.2V7zm0 2.8V17h16V9.8l-8 5.2z"/></svg>
          <span>info@velmarhall.org</span>
        </div>
        <div class="contact-line">
          <svg viewBox="0 0 24 24" aria-hidden="true"><path d="M12 2a10 10 0 1 0 0 20 10 10 0 0 0 0-20zm0 2a8 8 0 0 1 6.9 4H15l-2 2-3-1-2 3 2 3v3.9A8 8 0 0 1 4.1 10H7l2-3-1-2.6A8 8 0 0 1 12 4zm3 9 3 1.2-1 3.5A8 8 0 0 1 13 19.9V17z"/></svg>
          <span>www.velmarhall.org</span>
        </div>
      </div>
      <address class="contact contact-address" style="font-style: normal;">
        2-4-9 Kitasato,<br>
        Minato-ku, Tokyo, 150-0099
      </address>
    </footer>
  </main>
</body>
</html>
```